Stationary For Commercial Real Estate Company

We need a consistently branded image for our business cards, letterhead, property marketing flyers, powerpoint presentations, etc.

We are a COMMERCIAL real estate company. We do NOT do residential real estate, so please do not submit any designs with references to houses as they will be rejected.

We just completed a design contest for our logo, so we want to encorporate that logo in our stationary design, and we have attached it for your use. Please let us know if you need the logo in another format.

We can accept the business cards in adobe illustrator, the letterhead needs to be a template in Microsoft Word, the Property Flyer can be either in PowerPoint or Adobe Illustrator, and the PowerPoint presentation needs to have a Cover Page, Table of Contents, a few sample pages, and a Closing/Summary slide at the end.

We have attached a sample Property Flyer to show what we are basically looking for; but this is only provided as a sample, so you can see the kind of information we generally need to include on our Flyers. They can be in either landscape or portrait layout.

Target Market(s)

CEO and Upper Level managers who are decision makers regarding commercial real estate projects. Local, regional and fortune 500 clients.

Industry/Entity Type

Real Estate

Requirements
Must have
• There must be a space on the Flyer that includes the disclaimer shown on the bottom of the attached sample.
Nice to have
• I appreciate the designs submitted so far, but I'd prefer not to have watermarks on the letterhead or business cards. I'm not sure I'm a big fan of the watermarks.

Also, I'd like to see some color combinations that use something other than just red. I'd like to see something where we have just the logo in red and use other contrasting colors on the letterhead or business cards.
Should not have
• Please, no references to houses or anything else that suggests residential real estate. We only do commercial real estate.

```html
<!DOCTYPE html>
<html lang="en">
<head>
<meta charset="utf-8">
<title>Hollis Marrow Commercial Real Estate – Stationery</title>
<link rel="stylesheet" href="https://fonts.googleapis.com/css2?family=Arimo:wght@400;700&display=swap">
<style>
  :root {
    --brand-red: #b3202b;
    --brand-red-bright: #d81f35;
    --brand-red-deep: #9c1a26;
    --ink: #111111;
    --muted: #8a8f96;
    --label-blue: #5b7fa6;
    --body-grey: #6b6f75;
    --paper: #ffffff;
    --stage: #ecebe8;
    --tint-pink: #e9cfc9;
    --tint-teal: #7fc4c4;
  }
  * { box-sizing: border-box; margin: 0; padding: 0; }
  html, body { width: 1200px; height: 898px; overflow: hidden; }
  body {
    background: var(--stage);
    font-family: "Arimo", Arial, sans-serif;
    position: relative;
  }

  /* ---------- shared brand lockup ---------- */
  .brand { position: absolute; display: flex; flex-direction: column; }
  .brand-mark { background: var(--brand-red); }
  .brand-name, .brand-line {
    font-weight: 700;
    color: var(--ink);
    line-height: 1.05;
    white-space: nowrap;
  }

  .mosaic { position: absolute; }

  /* ---------- letterhead ---------- */
  .letterhead {
    position: absolute; left: 88px; top: 12px;
    width: 598px; height: 856px;
    background: var(--paper);
    box-shadow: 0 2px 8px rgba(0,0,0,.18);
  }
  .letterhead .brand { left: 58px; top: 38px; }
  .letterhead .brand-mark { width: 58px; height: 58px; margin: 0 0 26px 30px; }
  .letterhead .brand-name { font-size: 17px; }
  .letterhead .brand-line { font-size: 11.5px; }
  .letterhead .web {
    position: absolute; left: 265px; top: 42px;
    font-size: 10px; color: var(--muted);
  }
  .letterhead .mosaic-top {
    right: 0; top: 0; width: 130px; height: 120px;
    background: linear-gradient(225deg, var(--tint-pink) 0%, rgba(233,207,201,.4) 50%, rgba(255,255,255,0) 95%);
  }
  .letterhead .mosaic-bottom {
    left: 0; bottom: 0; width: 228px; height: 170px;
    background: linear-gradient(30deg, var(--tint-teal) 0%, #b9d6d2 35%, var(--tint-pink) 65%, rgba(255,255,255,0) 100%);
  }
  .contact {
    display: grid;
    grid-template-columns: auto auto;
    column-gap: 6px;
    font-size: 10px;
    line-height: 1.25;
    color: var(--body-grey);
  }
  .contact dt { color: var(--label-blue); }
  .letterhead .contact { position: absolute; left: 253px; top: 753px; }

  /* ---------- business card back (red) ---------- */
  .card { position: absolute; box-shadow: 0 2px 8px rgba(0,0,0,.25); overflow: hidden; }
  .card-back {
    left: 592px; top: 262px; width: 442px; height: 246px;
    background: radial-gradient(circle at 55% 55%, var(--brand-red-bright) 0%, var(--brand-red) 55%, var(--brand-red-deep) 100%);
  }
  .card-back .mosaic {
    left: 0; top: 72px; width: 150px; height: 174px;
    background: linear-gradient(20deg, var(--tint-teal) 0%, #9db8b0 40%, rgba(210,140,140,.5) 75%, rgba(200,40,50,0) 100%);
  }
  .card-back .brand { left: 74px; top: 88px; }
  .card-back .brand-mark {
    width: 56px; height: 56px; margin: 0 0 22px 30px; background: var(--paper);
  }
  .card-back .brand-name, .card-back .brand-line { color: var(--paper); }
  .card-back .brand-name { font-size: 17px; }
  .card-back .brand-line { font-size: 11.5px; }

  /* ---------- business card front (white) ---------- */
  .card-front {
    left: 716px; top: 470px; width: 446px; height: 252px;
    background: var(--paper);
  }
  .card-front .mosaic-top {
    right: 0; top: 0; width: 110px; height: 80px;
    background: linear-gradient(225deg, var(--tint-pink) 0%, rgba(233,207,201,.35) 55%, rgba(255,255,255,0) 100%);
  }
  .card-front .mosaic-bottom {
    left: 0; bottom: 0; width: 160px; height: 120px;
    background: linear-gradient(30deg, var(--tint-teal) 0%, #b9d6d2 40%, var(--tint-pink) 70%, rgba(255,255,255,0) 100%);
  }
  .card-front .brand { left: 28px; top: 36px; }
  .card-front .brand-mark { width: 52px; height: 52px; margin: 0 0 20px 20px; }
  .card-front .brand-name { font-size: 14px; }
  .card-front .brand-line { font-size: 9.5px; }
  .holder { position: absolute; left: 190px; top: 78px; }
  .holder-name { font-size: 19px; font-weight: 700; color: var(--brand-red); }
  .holder-role { font-size: 14px; color: var(--body-grey); margin-top: 2px; }
  .card-front .web {
    position: absolute; left: 192px; top: 130px; font-size: 8.5px; color: var(--muted);
  }
  .card-front .contact {
    position: absolute; left: 192px; top: 150px; font-size: 9px; line-height: 1.2;
  }
</style>
</head>
<body>

  <!-- Letterhead -->
  <section class="letterhead">
    <div class="mosaic mosaic-top" role="img" aria-label="Soft pink pixel-tile corner pattern"></div>
    <div class="brand">
      <div class="brand-mark"></div>
      <span class="brand-name">HOLLIS MARROW</span>
      <span class="brand-line">COMMERCIAL REAL ESTATE</span>
    </div>
    <p class="web">www.hollismarrowrealestate.com</p>
    <dl class="contact">
      <dt>Mobile:</dt><dd>(01) 12345678</dd>
      <dt>Tel:</dt><dd>(01) 12345678</dd>
      <dt>email:</dt><dd>email@hollismarrow.com</dd>
      <dt>Address:</dt><dd>Address name 1234 Address line 2 01234<br>State, Region, Country</dd>
    </dl>
    <div class="mosaic mosaic-bottom" role="img" aria-label="Teal to pink pixel-tile corner pattern"></div>
  </section>

  <!-- Business card, back -->
  <section class="card card-back">
    <div class="mosaic" role="img" aria-label="Teal pixel-tile pattern fading into red"></div>
    <div class="brand">
      <div class="brand-mark"></div>
      <span class="brand-name">HOLLIS MARROW</span>
      <span class="brand-line">COMMERCIAL REAL ESTATE</span>
    </div>
  </section>

  <!-- Business card, front -->
  <section class="card card-front">
    <div class="mosaic mosaic-top" role="img" aria-label="Soft pink pixel-tile corner pattern"></div>
    <div class="mosaic mosaic-bottom" role="img" aria-label="Teal to pink pixel-tile corner pattern"></div>
    <div class="brand">
      <div class="brand-mark"></div>
      <span class="brand-name">HOLLIS MARROW</span>
      <span class="brand-line">COMMERCIAL REAL ESTATE</span>
    </div>
    <div class="holder">
      <p class="holder-name">Name Surname</p>
      <p class="holder-role">Marketing Manager</p>
    </div>
    <p class="web">www.hollismarrowrealestate.com</p>
    <dl class="contact">
      <dt>Mobile:</dt><dd>(01) 12345678</dd>
      <dt>Tel:</dt><dd>(01) 12345678</dd>
      <dt>email:</dt><dd>email@hollismarrow.com</dd>
      <dt>Address:</dt><dd>Address name 1234<br>Address line 2 01234<br>State, Region, Country</dd>
    </dl>
  </section>

</body>
</html>
```